2 Stellenanzeigenbanner für Personaldienstleister zur Werbung auf Promotion-Jobplattform
Die Qualität der Arbeiten war sehr gut. Die Kommunikation mit dem Designer klappte hervorragend. Wir können eine Zusammenarbeit absolut empfehlen!
Zielgruppe
Unser Unternehmen ist primär im Bereich der personalgestützten Absatzförderung am Point of Sale (PoS) mit Schwerpunkt Sales Promotion tätig. Die Zielgruppe der Banner als einzusetzende Werbemittel besteht in erster Linie aus Freiberuflern aus den Bereichen Verkauf und Promotion, die als Markenbotschafter und Fachberater im Auftrag unserer Kunden an den Verkaufspunkten agieren.
Aufgabenstellung
Zur Veröffentlichung auf einer bekannten Promotion-Jobplattform müssen 2 statische Banner in den Formaten 1) 160 x 600 und 2) 468 x 60 erstellt werden, die zu einer Stellenausschreibung führen. Die Banner müssen das offizielle Logo der Agentur sowie die Unternehmensfarben (Rot & Blau) beinhalten und gemeinsam ein einheitliches Design bilden. Die zu verwendenden Textinhalte finden sich in den Anhängen "Text 1" und "Text 2", können vom Designer aber frei angepasst werden.

```html
<!DOCTYPE html>
<html lang="de">
<head>
<meta charset="utf-8">
<title>Stellenanzeigenbanner – Sales Promoter & Fachberater</title>
<link rel="stylesheet" href="https://fonts.googleapis.com/css2?family=Open+Sans:wght@300;400;600;700&display=swap">
<style>
  :root {
    --brand-blue: #0d4a6e;
    --brand-red: #9a1232;
    --white: #ffffff;
    --paper: #ffffff;
    --frame: #e6e6e6;
    --sky-top: #b9b4a6;
    --sky-mid: #8d8f86;
    --land: #5d6a52;
    --road: #6f6f6c;
  }
  * { box-sizing: border-box; margin: 0; padding: 0; }
  html, body { width: 1200px; height: 1200px; overflow: hidden; background: var(--paper); }
  body { position: relative; font-family: "Open Sans", Arial, sans-serif; }

  .skyscraper {
    position: absolute; top: 169px; width: 190px; height: 718px;
    border: 1px solid var(--frame); overflow: hidden; background: var(--white);
  }
  .skyscraper.solo { left: 60px; }
  .skyscraper.duo { left: 288px; }

  .skyscraper .photo {
    position: absolute; left: 0; top: 0; width: 100%; height: 648px;
    background: linear-gradient(180deg, var(--sky-top) 0%, var(--sky-mid) 45%, var(--land) 68%, var(--road) 100%);
  }
  .skyscraper .header { position: absolute; left: 0; top: 0; width: 190px; height: 90px; }
  .skyscraper .header-text {
    position: absolute; left: 0; top: 14px; width: 100%; text-align: center;
    color: var(--white); font-weight: 700; font-size: 19px; line-height: 24px;
  }
  .skyscraper .headline {
    position: absolute; left: 0; top: 104px; width: 100%; text-align: center;
    color: var(--white); font-weight: 400; font-size: 21px; line-height: 29px; letter-spacing: 0.5px;
  }
  .skyscraper .cta { position: absolute; left: 0; top: 515px; width: 190px; height: 133px; }
  .skyscraper .cta-text {
    position: absolute; left: 10px; top: 540px; color: var(--white);
    transform: rotate(-5deg); transform-origin: left top;
  }
  .cta-small { display: block; font-weight: 600; font-size: 15px; line-height: 18px; letter-spacing: 0.3px; }
  .cta-big { display: block; font-weight: 700; font-size: 22px; line-height: 26px; }
  .skyscraper .brand {
    position: absolute; left: 0; top: 664px; width: 100%; text-align: center;
  }
  .brand-name {
    display: inline-flex; align-items: center; gap: 6px;
    color: var(--brand-blue); font-weight: 700; font-size: 19px; letter-spacing: 0.5px;
  }
  .brand-dot { width: 9px; height: 9px; border-radius: 50%; background: var(--brand-red); }
  .brand-claim {
    display: block; margin-top: 4px; color: var(--brand-red);
    font-weight: 600; font-size: 8px; letter-spacing: 2.2px;
  }

  .leaderboard {
    position: absolute; left: 565px; width: 560px; height: 70px;
    border: 1px solid var(--frame); overflow: hidden; background: var(--white);
  }
  .leaderboard.first { top: 169px; }
  .leaderboard.second { top: 277px; }
  .leaderboard.third { top: 385px; }
  .leaderboard .photo {
    position: absolute; left: 0; top: 0; width: 440px; height: 100%;
    background: linear-gradient(180deg, var(--sky-top) 0%, var(--sky-mid) 55%, var(--land) 85%, var(--road) 100%);
  }
  .leaderboard svg.shapes { position: absolute; left: 0; top: 0; }
  .leaderboard .header-text {
    position: absolute; left: 0; top: 9px; width: 78px; text-align: center;
    color: var(--white); font-weight: 700; font-size: 13px; line-height: 17px;
  }
  .leaderboard .headline {
    position: absolute; left: 95px; top: 8px; color: var(--white);
    font-weight: 600; font-size: 14px; line-height: 17px; letter-spacing: 0.4px;
  }
  .leaderboard .cta-text {
    position: absolute; left: 325px; top: 14px; color: var(--white);
  }
  .leaderboard .cta-small { font-size: 11px; line-height: 14px; }
  .leaderboard .cta-big { font-size: 16px; line-height: 20px; }
  .leaderboard .brand {
    position: absolute; left: 440px; top: 0; width: 120px; height: 100%;
    display: flex; align-items: center; justify-content: center;
  }
  .leaderboard .brand-name { font-size: 16px; }
</style>
</head>
<body>

  <section class="skyscraper solo" aria-label="Banner 160 x 600, Variante Promoterin">
    <div class="photo" role="img" aria-label="Foto: eine Promoterin in weißer Bluse und Jeans springt vor einer Landschaft mit See und bewölktem Himmel los"></div>
    <svg class="header" viewBox="0 0 190 90" aria-hidden="true"><polygon points="0,0 190,0 190,68 95,90 0,68" fill="var(--brand-blue)"/></svg>
    <p class="header-text">WIR SUCHEN<br>DICH!</p>
    <p class="headline">SALES<br>PROMOTER &amp;<br>FACHBERATER<br>AUFGEPASST!</p>
    <svg class="cta" viewBox="0 0 190 133" aria-hidden="true"><polygon points="0,40 132,26 132,0 190,62 132,133 132,112 0,124" fill="var(--brand-red)"/></svg>
    <p class="cta-text"><span class="cta-small">JETZT SCHNELL</span><span class="cta-big">BEWERBEN</span></p>
    <div class="brand">
      <span class="brand-name"><span class="brand-dot"></span>EILWERK</span>
      <span class="brand-claim">PERSONAL FÜR DEN HANDEL</span>
    </div>
  </section>

  <section class="skyscraper duo" aria-label="Banner 160 x 600, Variante Promoterin und Fachberater">
    <div class="photo" role="img" aria-label="Foto: ein Fachberater mit Brille und eine Promoterin springen gemeinsam vor einer Landschaft mit See los"></div>
    <svg class="header" viewBox="0 0 190 90" aria-hidden="true"><polygon points="0,0 190,0 190,68 95,90 0,68" fill="var(--brand-blue)"/></svg>
    <p class="header-text">WIR SUCHEN<br>DICH!</p>
    <p class="headline">SALES<br>PROMOTER &amp;<br>FACHBERATER<br>AUFGEPASST!</p>
    <svg class="cta" viewBox="0 0 190 133" aria-hidden="true"><polygon points="0,40 132,26 132,0 190,62 132,133 132,112 0,124" fill="var(--brand-red)"/></svg>
    <p class="cta-text"><span class="cta-small">JETZT SCHNELL</span><span class="cta-big">BEWERBEN</span></p>
    <div class="brand">
      <span class="brand-name"><span class="brand-dot"></span>EILWERK</span>
      <span class="brand-claim">PERSONAL FÜR DEN HANDEL</span>
    </div>
  </section>

  <section class="leaderboard first" aria-label="Banner 468 x 60, Variante Promoterin">
    <div class="photo" role="img" aria-label="Foto: springende Promoterin vor einer Seelandschaft"></div>
    <svg class="shapes" width="560" height="70" viewBox="0 0 560 70" aria-hidden="true">
      <polygon points="0,0 78,0 90,35 78,70 0,70" fill="var(--brand-blue)"/>
      <polygon points="316,12 408,12 408,0 442,35 408,70 408,58 316,58" fill="var(--brand-red)"/>
    </svg>
    <p class="header-text">WIR<br>SUCHEN<br>DICH</p>
    <p class="headline">SALES PROMOTER<br>&amp; FACHBERATER<br>AUFGEPASST!</p>
    <p class="cta-text"><span class="cta-small">JETZT SCHNELL</span><span class="cta-big">BEWERBEN</span></p>
    <div class="brand"><span class="brand-name"><span class="brand-dot"></span>EILWERK</span></div>
  </section>

  <section class="leaderboard second" aria-label="Banner 468 x 60, Variante Fachberater">
    <div class="photo" role="img" aria-label="Foto: springender Fachberater vor einer Seelandschaft"></div>
    <svg class="shapes" width="560" height="70" viewBox="0 0 560 70" aria-hidden="true">
      <polygon points="0,0 78,0 90,35 78,70 0,70" fill="var(--brand-blue)"/>
      <polygon points="316,12 408,12 408,0 442,35 408,70 408,58 316,58" fill="var(--brand-red)"/>
    </svg>
    <p class="header-text">WIR<br>SUCHEN<br>DICH</p>
    <p class="headline">SALES PROMOTER<br>&amp; FACHBERATER<br>AUFGEPASST!</p>
    <p class="cta-text"><span class="cta-small">JETZT SCHNELL</span><span class="cta-big">BEWERBEN</span></p>
    <div class="brand"><span class="brand-name"><span class="brand-dot"></span>EILWERK</span></div>
  </section>

  <section class="leaderboard third" aria-label="Banner 468 x 60, Variante Promoterin und Fachberater">
    <div class="photo" role="img" aria-label="Foto: Fachberater und Promoterin springen gemeinsam vor einer Seelandschaft los"></div>
    <svg class="shapes" width="560" height="70" viewBox="0 0 560 70" aria-hidden="true">
      <polygon points="0,0 78,0 90,35 78,70 0,70" fill="var(--brand-blue)"/>
      <polygon points="316,12 408,12 408,0 442,35 408,70 408,58 316,58" fill="var(--brand-red)"/>
    </svg>
    <p class="header-text">WIR<br>SUCHEN<br>DICH</p>
    <p class="headline">SALES PROMOTER<br>&amp; FACHBERATER<br>AUFGEPASST!</p>
    <p class="cta-text"><span class="cta-small">JETZT SCHNELL</span><span class="cta-big">BEWERBEN</span></p>
    <div class="brand"><span class="brand-name"><span class="brand-dot"></span>EILWERK</span></div>
  </section>

</body>
</html>
```